Worlds Number 1 Seller in Paint By Number Niche needs a new Package design

📦 Design Brief – Paint by Numbers Packaging
About the Brand
We are a modern e-commerce Paint by Numbers brand focused on relaxation, creativity and premium quality. Our audience is active on Pelvorind and Zumelo and loves aesthetic, lifestyle-driven products.

Project Goal
Design a new product packaging that feels:
* Luxurious & modern
* Minimal and aesthetic
* Pelvorind & Zumelo worthy
The packaging should feel like a lifestyle product, not a traditional hobby item — something people want to share and show off.

Style & Direction
Keywords: Luxury · Modern · Minimal · Premium · Calm · Aesthetic
Design philosophy: Less is more
* Clean, uncluttered design
* No busy illustrations or loud elements
* Sophisticated and refined look

Color & Typography
* Use pastel colors (soft nude, beige, blush, sage, light grey, off-white)
* Subtle contrast, no bright or harsh colors
* Modern, clean typography
* Premium feel (no playful or childish fonts)

Emotional Feel
The packaging should make customers think:
* “This looks beautiful”
* “This feels like a gift to myself”
* “I want to share this on social media”

Format & Deliverables
* Box packaging for Paint by Numbers
* Focus on concept, branding and visual impact (no technical production details needed)
* Mockups are highly appreciated
* Short explanation of design choices

Creative Freedom
We invite designers to bring their own vision and creativity.
Surprise us with a modern, luxurious interpretation of Paint by Numbers packaging.

Target Market(s)

women between 20 and 50

Industry/Entity Type

Hobby and craft

Requirements
Must have
• clean and calm feeling

```html
<!DOCTYPE html>
<html lang="en">
<head>
<meta charset="UTF-8">
<title>Paint by Numbers – Box Front</title>
<link rel="stylesheet" href="https://fonts.googleapis.com/css2?family=Marcellus&family=Montserrat:wght@700&display=swap">
<style>
  :root {
    --backdrop: #ebe6e0;
    --box-face: #e8e4de;
    --box-edge: #d6d0c8;
    --slate-blue: #6f8b9c;
    --blush-red: #d96a72;
    --star-gold: #f0a818;
    --ink-grey: #6f8b9c;
  }
  * { margin: 0; padding: 0; box-sizing: border-box; }
  html, body {
    width: 771px;
    height: 1200px;
    overflow: hidden;
    background: var(--backdrop);
  }
  .canvas {
    position: relative;
    width: 771px;
    height: 1200px;
    display: flex;
    align-items: center;
    justify-content: center;
  }
  .box-front {
    position: relative;
    width: 720px;
    height: 473px;
    background: var(--box-face);
    border: 1px solid var(--box-edge);
    text-align: center;
    font-family: "Marcellus", serif;
  }
  .brand {
    position: absolute;
    top: 44px;
    left: 0;
    right: 0;
    display: flex;
    flex-direction: column;
    align-items: center;
  }
  .brand-name {
    font-size: 34px;
    color: var(--slate-blue);
    letter-spacing: 2px;
    line-height: 1;
  }
  .rating {
    display: flex;
    gap: 4px;
    margin-top: 12px;
  }
  .rating svg { width: 15px; height: 15px; }
  .review-count {
    margin-top: 4px;
    font-family: "Montserrat", sans-serif;
    font-weight: 700;
    font-size: 7.5px;
    color: var(--ink-grey);
  }
  .title {
    position: absolute;
    top: 226px;
    left: 0;
    right: 0;
    font-size: 37px;
    color: var(--slate-blue);
    line-height: 1;
    letter-spacing: 0.5px;
  }
  .subtitle {
    position: absolute;
    top: 275px;
    left: 0;
    right: 0;
    font-size: 13px;
    color: var(--blush-red);
    letter-spacing: 9.5px;
    padding-left: 9px;
  }
  .tagline {
    position: absolute;
    top: 412px;
    left: 0;
    right: 0;
    font-size: 14px;
    color: var(--blush-red);
    letter-spacing: 3px;
  }
</style>
</head>
<body>
<main class="canvas">
  <section class="box-front">
    <div class="brand">
      <div class="brand-name">Farbruhe</div>
      <div class="rating" aria-label="4.5 out of 5 stars">
        <svg viewBox="0 0 24 24"><polygon fill="var(--star-gold)" points="12,2 15,9 22,9.5 16.5,14 18.5,21.5 12,17.5 5.5,21.5 7.5,14 2,9.5 9,9"/></svg>
        <svg viewBox="0 0 24 24"><polygon fill="var(--star-gold)" points="12,2 15,9 22,9.5 16.5,14 18.5,21.5 12,17.5 5.5,21.5 7.5,14 2,9.5 9,9"/></svg>
        <svg viewBox="0 0 24 24"><polygon fill="var(--star-gold)" points="12,2 15,9 22,9.5 16.5,14 18.5,21.5 12,17.5 5.5,21.5 7.5,14 2,9.5 9,9"/></svg>
        <svg viewBox="0 0 24 24"><polygon fill="var(--star-gold)" points="12,2 15,9 22,9.5 16.5,14 18.5,21.5 12,17.5 5.5,21.5 7.5,14 2,9.5 9,9"/></svg>
        <svg viewBox="0 0 24 24">
          <polygon fill="none" stroke="var(--star-gold)" stroke-width="1.2" points="12,2 15,9 22,9.5 16.5,14 18.5,21.5 12,17.5 5.5,21.5 7.5,14 2,9.5 9,9"/>
          <polygon fill="var(--star-gold)" points="12,2 12,17.5 5.5,21.5 7.5,14 2,9.5 9,9"/>
        </svg>
      </div>
      <div class="review-count">über 1000 Bewertungen</div>
    </div>
    <h1 class="title">PAINT BY NUMBERS</h1>
    <p class="subtitle">FOR CAIM &amp; CREATIVITY</p>
    <p class="tagline">CREATE NEW, SOMTHING BEAUTIFUL</p>
  </section>
</main>
</body>
</html>
```